DL flyer front and back + magnet

DL Flyer Design Brief – VKD Plumbing

Objective:
Create a bold, high-impact DL flyer promoting a Blocked Drain Special to generate immediate service calls.

Main Headline (Large & Eye Catching)

🚨 BLOCKED DRAIN SPECIAL – $299 🚨

High Pressure Water Jetting

Offer Details

💧 Clear stubborn blocked drains fast
💧 Professional high-pressure water jetting
💧 Removes tree roots, grease & debris

Limited Time Bonus

⭐ FIRST 15 CALLS RECEIVE A FREE CCTV CAMERA INSPECTION
(Valued at $149)

Trust Points (Icons or Ticks)

✔ Local Licensed Plumbers
✔ Fast Same Day Service
✔ Upfront Pricing
✔ 5 Star Rated Service

Call To Action (Very Prominent)

📞 CALL NOW TO BOOK
Limited bookings available

Phone: 0491 570 006
Website: vkdplumbing.com.au

Branding

Include:

VKD Plumbing logo

Plumbing imagery (blocked drain / jetting hose)

Use brand colours from VKD logo
💡 Design Tip:
The $299 price should be the biggest element on the flyer so people instantly see the offer.

Back Side Layout – VKD Plumbing Flyer
🏠 Your Local Trusted Plumber

Fast, Reliable Plumbing Services Across the Sutherland Shire

We provide professional plumbing services for homes and businesses including:

Our Services

✔ Blocked Drains
✔ Leak Detection & Repairs
✔ Hot Water Systems
✔ Tap & Toilet Repairs
✔ Stormwater Repairs
✔ CCTV Drain Inspections
✔ Gutter & Roof Plumbing
✔ Preventative Plumbing Maintenance

⭐ Why Choose VKD Plumbing?

✔ Fully Licensed & Insured
✔ Upfront Honest Pricing
✔ Fast Local Service
✔ Clean & Professional Workmanship
✔ Trusted by Local Homeowners & Businesses

⭐ What Our Customers Say

⭐⭐⭐⭐⭐
"Lachlan from VKD Plumbing cleared our blocked drain quickly and professionally. Highly recommend!"

⭐⭐⭐⭐⭐
"Prompt, reliable and great service. Will definitely use again."

(Fintaro Ratings)

📞 Need a Plumber?

VKD Plumbing

📞 Call: 0491 570 006
🌐 vkdplumbing.com.au

Add this small section on the back:

Neighbour Discount

💧 $59 OFF ANY PLUMBING REPAIR
(Mention this flyer when booking)

Magnet should be similar to these

```html
<!DOCTYPE html>
<html lang="en">
<head>
<meta charset="utf-8">
<title>VKD Plumbing – DL Flyer Front, Back &amp; Magnet</title>
<link href="https://fonts.googleapis.com/css2?family=Montserrat:ital,wght@0,400;0,500;0,600;0,700;0,800;0,900;1,400;1,500&display=swap" rel="stylesheet">
<style>
:root{
  --blue:#2bb8e3;
  --yellow:#f5bf3a;
  --dark:#333538;
  --paper:#ececec;
  --board:#666666;
  --white:#ffffff;
}
*{box-sizing:border-box;margin:0;padding:0}
html,body{width:1198px;height:1200px;overflow:hidden;background:var(--board)}
body{position:relative;font-family:'Montserrat',sans-serif;color:var(--dark)}
.defs{position:absolute;width:0;height:0;overflow:hidden}
.sheet{position:absolute;background:var(--paper);overflow:hidden}
.abs{position:absolute}
.flyer-front{left:205px;top:107px;width:342px;height:726px}
.flyer-back{left:651px;top:107px;width:342px;height:726px}
.magnet{left:658px;top:891px;width:328px;height:196px}

.brand{position:absolute;color:var(--blue);font-weight:800;letter-spacing:-.5px;white-space:nowrap;line-height:1}

/* front */
.front-band{left:0;top:122px;width:342px;height:166px;background:var(--blue)}
.front-hero{left:190px;top:-12px;width:190px;height:248px}
.front-hose{left:182px;top:118px;width:96px;height:128px}
.headline{left:9px;top:133px;color:var(--white);font-weight:800;font-size:32px;letter-spacing:.5px;line-height:1}
.subhead{left:9px;top:166px;color:var(--yellow);font-weight:800;font-size:20px;line-height:1}
.price{left:9px;top:196px;width:165px;height:60px;background:var(--dark);border-radius:0 30px 30px 0;color:var(--white);font-weight:800;font-size:58px;line-height:60px;padding-left:26px;letter-spacing:-1px}
.price sup{position:absolute;left:8px;top:-14px;font-size:26px}
.jetting{left:11px;top:267px;color:var(--white);font-weight:600;font-size:17px;line-height:1}
.offer-list{left:9px;top:303px;list-style:none;font-weight:700;font-size:14px;line-height:22px}
.offer-list li{display:flex;gap:6px;align-items:flex-start}
.offer-list svg{flex:none;margin-top:6px}
.bonus-box{left:99px;top:422px;width:232px;height:68px;border:2px solid var(--yellow);border-radius:6px}
.bonus-badge{left:9px;top:406px;width:104px;height:104px}
.bonus-badge span{position:absolute;inset:0;display:flex;align-items:center;justify-content:center;text-align:center;color:var(--white);font-weight:800;font-size:17px;line-height:17px}
.bonus-line{left:117px;top:430px;font-size:14px;font-weight:500;white-space:nowrap}
.bonus-free{left:117px;top:447px;font-size:11px;font-weight:800;color:var(--yellow);white-space:nowrap}
.bonus-value{left:118px;top:461px;background:var(--dark);color:var(--white);font-weight:800;font-size:16px;padding:1px 5px;border-radius:0 10px 10px 0}
.trust{left:0;top:498px;width:342px;height:162px;background:var(--blue)}
.trust-rule{left:10px;top:518px;width:322px;height:2px;background:var(--yellow)}
.trust-pill{left:104px;top:508px;width:132px;height:22px;background:var(--yellow);border-radius:11px;color:var(--white);font-weight:800;font-size:14px;text-align:center;line-height:22px}
.trust-item{width:170px;text-align:center;color:var(--white);font-weight:700;font-size:11px}
.trust-item svg{display:block;margin:0 auto 6px}
.cta{left:73px;top:644px;width:196px;height:23px;background:var(--yellow);border-radius:12px;color:var(--white);font-weight:800;font-size:14px;line-height:23px;display:flex;justify-content:center;gap:6px;align-items:center}
.cta-note{left:0;top:670px;width:342px;text-align:center;font-size:10px}
.front-phone{left:11px;top:695px;font-size:21px;font-weight:600;display:flex;align-items:center;gap:3px;white-space:nowrap}
.front-web{right:9px;top:702px;font-size:11.5px;font-weight:500;display:flex;align-items:center;gap:3px;white-space:nowrap}

/* back */
.portrait{left:-6px;top:-60px;width:172px;height:350px}
.tag-band{left:122px;top:53px;width:220px;height:67px;background:var(--blue);clip-path:polygon(0 0,100% 0,100% 100%,17% 100%)}
.tag-title{left:166px;top:60px;color:var(--yellow);font-weight:800;font-size:13px;line-height:15px;white-space:nowrap}
.tag-sub{left:166px;top:91px;color:var(--white);font-weight:600;font-size:9.5px;line-height:13px;white-space:nowrap}
.why{left:162px;top:225px;width:172px;height:232px;background:var(--yellow);border-radius:8px;transform:rotate(-1deg)}
.why-title{left:181px;top:235px;color:var(--white);font-weight:800;font-size:14px;line-height:16px}
.why-list{left:172px;top:278px;list-style:none;color:var(--white);font-weight:500;font-size:12px;line-height:16.8px;width:160px}
.why-list li{display:flex;gap:3px}
.why-list svg{flex:none;margin-top:3px}
.services-pill{left:11px;top:316px;width:124px;height:20px;background:var(--dark);border-radius:0 10px 10px 0;color:var(--white);font-weight:800;font-size:14px;line-height:20px;padding-left:4px}
.services-list{left:10px;top:340px;list-style:none;font-size:12.5px;line-height:20.8px;font-weight:500;width:165px}
.services-list li{display:flex;gap:5px;white-space:nowrap}
.services-list svg{flex:none;margin-top:5px}
.reviews-pill{left:174px;top:467px;width:143px;height:37px;background:var(--dark);border-radius:0 18px 18px 0;color:var(--white);font-weight:800;font-size:13px;line-height:15px;padding:4px 0 0 5px}
.review{left:174px;width:162px;text-align:center;font-size:9px;font-style:italic;line-height:10px}
.stars{color:var(--yellow);font-style:normal;font-size:10px;letter-spacing:1px;margin-bottom:2px}
.contact-box{left:0;top:618px;width:170px;height:99px;background:var(--blue);color:var(--white);padding:10px 0 0 13px}
.contact-box .q{font-weight:800;font-size:15px}
.contact-box .n{font-size:15px;margin-left:20px;font-weight:500}
.contact-box .line{display:flex;align-items:center;gap:3px;font-size:13px;font-weight:500;margin-top:4px;white-space:nowrap}
.discount{left:178px;top:618px;width:155px;height:99px;border:3px solid var(--yellow);text-align:center}
.discount .t{font-weight:700;font-size:9px;margin-top:6px}
.discount .big{display:flex;justify-content:center;align-items:center;gap:2px;color:var(--yellow);height:50px;font-weight:900}
.discount .cur{font-size:24px;align-self:flex-start;margin-top:4px}
.discount .num{font-size:50px;line-height:50px;letter-spacing:-1px}
.discount .off{writing-mode:vertical-rl;font-size:13px;letter-spacing:1px;line-height:1}
.discount .r{font-weight:700;font-size:9.5px}
.discount .m{font-style:italic;font-size:7px;margin-top:2px}

/* magnet */
.mag-art{left:180px;top:0;width:148px;height:196px}
.mag-band{left:0;top:92px;width:190px;height:64px;background:var(--blue)}
.mag-foot{left:0;top:156px;width:190px;height:40px;background:var(--yellow)}
.mag-q{left:24px;top:96px;color:var(--white);font-weight:800;font-size:17px}
.mag-call{left:24px;top:117px;color:var(--white);font-size:13px;font-weight:500}
.mag-call b{color:var(--yellow);font-weight:700}
.mag-phone{left:23px;top:134px;color:var(--white);font-weight:800;font-size:15px;display:flex;align-items:center;gap:3px}
.mag-web{left:24px;top:168px;color:var(--white);font-size:11px;font-weight:500;display:flex;align-items:center;gap:3px}
</style>
</head>
<body>

<svg class="defs" aria-hidden="true">
  <defs>
    <symbol id="teardrop" viewBox="0 0 100 140"><path d="M50 0 C60 25 100 58 100 90 A50 50 0 0 1 0 90 C0 58 40 25 50 0Z"/></symbol>
    <symbol id="droplet" viewBox="0 0 10 14"><path d="M5 0C6 3 10 6 10 9A5 5 0 0 1 0 9C0 6 4 3 5 0Z"/></symbol>
    <symbol id="phone" viewBox="0 0 24 24"><path d="M6.6 10.8a15 15 0 0 0 6.6 6.6l2.2-2.2a1 1 0 0 1 1-.25 11.4 11.4 0 0 0 3.6.57 1 1 0 0 1 1 1V20a1 1 0 0 1-1 1A17 17 0 0 1 3 4a1 1 0 0 1 1-1h3.5a1 1 0 0 1 1 1c0 1.25.2 2.45.57 3.57a1 1 0 0 1-.25 1z"/></symbol>
    <symbol id="globe" viewBox="0 0 24 24"><circle cx="12" cy="12" r="9" fill="none" stroke="currentColor" stroke-width="2"/><path d="M3 12h18M12 3c3 3 3 15 0 18M12 3c-3 3-3 15 0 18" fill="none" stroke="currentColor" stroke-width="1.6"/></symbol>
    <symbol id="tickdrop" viewBox="0 0 12 14"><path d="M6 1C7 4 11 6.5 11 9a5 5 0 0 1-10 0C1 6.5 5 4 6 1Z" fill="none" stroke="currentColor" stroke-width="1.3"/><path d="M3.5 9l2 2 4-5" fill="none" stroke="currentColor" stroke-width="1.3"/></symbol>
    <linearGradient id="pipeShot" x1="0" y1="0" x2="1" y2="1">
      <stop offset="0" stop-color="#e9eef2"/><stop offset=".45" stop-color="#9fb3c0"/><stop offset=".7" stop-color="#a0603a"/><stop offset="1" stop-color="#d8dde1"/>
    </linearGradient>
    <linearGradient id="hoseShot" x1="0" y1="0" x2="0" y2="1">
      <stop offset="0" stop-color="#f4f4f4"/><stop offset=".5" stop-color="#2a2c30"/><stop offset="1" stop-color="#dfe9ef"/>
    </linearGradient>
    <linearGradient id="portraitShot" x1="0" y1="0" x2="0" y2="1">
      <stop offset="0" stop-color="#2bb8e3"/><stop offset=".35" stop-color="#2bb8e3"/><stop offset=".45" stop-color="#b98a6e"/><stop offset=".6" stop-color="#1f2a44"/><stop offset="1" stop-color="#1f2a44"/>
    </linearGradient>
  </defs>
</svg>

<!-- FRONT -->
<section class="sheet flyer-front">
  <div class="brand" style="left:11px;top:36px;font-size:27px">VKD Plumbing</div>

  <div class="abs front-band"></div>

  <svg class="abs front-hero" viewBox="0 0 100 140" preserveAspectRatio="none" role="img" aria-label="Photo of a chrome drain pipe with blocked debris and water inside">
    <use href="#teardrop" fill="var(--yellow)"/>
    <g transform="translate(6 8) scale(.88)"><use href="#teardrop" fill="url(#pipeShot)"/></g>
  </svg>
  <svg class="abs front-hose" viewBox="0 0 100 140" preserveAspectRatio="none" role="img" aria-label="Photo of a coiled high-pressure jetting hose">
    <use href="#teardrop" fill="var(--yellow)"/>
    <g transform="translate(8 10) scale(.84)"><use href="#teardrop" fill="#ffffff"/></g>
    <g transform="translate(14 18) scale(.72)"><use href="#teardrop" fill="url(#hoseShot)"/></g>
  </svg>

  <div class="abs headline">BLOCKED</div>
  <div class="abs subhead">DRAIN SPECIAL</div>
  <div class="abs price"><sup>$</sup>299</div>
  <div class="abs jetting">HIGH PRESSURE WATER JETTING</div>

  <ul class="abs offer-list">
    <li><svg width="8" height="11" fill="var(--blue)"><use href="#droplet"/></svg>Clear stubborn blocked drains fast</li>
    <li><svg width="8" height="11" fill="var(--blue)"><use href="#droplet"/></svg>Professional high-pressure water jetting</li>
    <li><svg width="8" height="11" fill="var(--blue)"><use href="#droplet"/></svg>Removes tree roots, grease &amp;<br>debris</li>
  </ul>

  <div class="abs bonus-box"></div>
  <div class="abs bonus-badge">
    <svg width="104" height="104" viewBox="0 0 104 104"><path fill="var(--blue)" d="M52 2l9 6 10-3 6 9 11 1 2 10 9 5-2 10 6 8-6 8 2 10-9 5-2 10-11 1-6 9-10-3-9 6-9-6-10 3-6-9-11-1-2-10-9-5 2-10-6-8 6-8-2-10 9-5 2-10 11-1 6-9 10 3z"/></svg>
    <span>Limited<br>Time<br>Bonus</span>
  </div>
  <div class="abs bonus-line">FIRST 15 CALLS RECEIVE A</div>
  <div class="abs bonus-free">FREE CCTV CAMERA INSPECTION</div>
  <div class="abs bonus-value">Valued at $149</div>

  <div class="abs trust"></div>
  <div class="abs trust-rule"></div>
  <div class="abs trust-pill">TRUST POINTS</div>
  <div class="abs trust-item" style="left:0;top:540px">
    <svg width="16" height="19" color="#fff"><use href="#tickdrop"/></svg>Local Licensed Plumbers</div>
  <div class="abs trust-item" style="left:172px;top:540px">
    <svg width="22" height="19" viewBox="0 0 22 19" fill="none" stroke="#fff" stroke-width="1.6"><circle cx="14" cy="11" r="6"/><path d="M14 8v3l2 1M1 8h6M3 11h5M1 14h6M12 3h4"/></svg>Fast Same Day Service</div>
  <div class="abs trust-item" style="left:0;top:590px">
    <svg width="20" height="19" viewBox="0 0 20 19" fill="#fff"><path d="M2 10L11 1h7v7l-9 9z"/><circle cx="15" cy="4" r="1.5" fill="var(--blue)"/></svg>Upfront Pricing</div>
  <div class="abs trust-item" style="left:172px;top:590px">
    <svg width="22" height="19" viewBox="0 0 22 19" fill="#fff"><rect x="1" y="1" width="20" height="4" fill="none" stroke="#fff"/><path d="M6 18V11h3l3-5c2 0 2 2 1 4h4c1 0 2 1 1.6 2l-1.2 5c-.2.7-.8 1-1.5 1z"/></svg>5 Star Rated Service</div>

  <div class="abs cta"><svg width="14" height="14" fill="#fff"><use href="#phone"/></svg>CALL NOW TO BOOK</div>
  <div class="abs cta-note">Limited bookings available</div>
  <div class="abs front-phone"><svg width="16" height="16" fill="var(--yellow)"><use href="#phone"/></svg>0491 570 006</div>
  <div class="abs front-web"><svg width="11" height="11" color="var(--yellow)"><use href="#globe"/></svg>vkdplumbing.com.au</div>
</section>

<!-- BACK -->
<section class="sheet flyer-back">
  <svg class="abs portrait" viewBox="0 0 100 140" preserveAspectRatio="none" role="img" aria-label="Portrait photo of Lachlan, the plumber, in a navy branded polo shirt">
    <use href="#teardrop" fill="var(--yellow)"/>
    <g transform="translate(5 6) scale(.9)"><use href="#teardrop" fill="url(#portraitShot)"/></g>
  </svg>

  <div class="abs tag-band"></div>
  <div class="abs tag-title">YOUR LOCAL TRUSTED<br>PLUMBER</div>
  <div class="abs tag-sub">Fast, Reliable Plumbing Services<br>Across the Sutherland Shire</div>

  <div class="brand" style="left:181px;top:160px;font-size:20px">VKD Plumbing</div>

  <div class="abs why"></div>
  <div class="abs why-title">WHY CHOOSE<br>VKD PLUMBING?</div>
  <ul class="abs why-list">
    <li><svg width="8" height="11" fill="var(--blue)"><use href="#droplet"/></svg>Fully Licensed &amp;<br>Insured</li>
    <li><svg width="8" height="11" fill="var(--blue)"><use href="#droplet"/></svg>Upfront Honest<br>Pricing</li>
    <li><svg width="8" height="11" fill="var(--blue)"><use href="#droplet"/></svg>Fast Local Service</li>
    <li><svg width="8" height="11" fill="var(--blue)"><use href="#droplet"/></svg>Clean &amp; Professional<br>Workmanship</li>
    <li><svg width="8" height="11" fill="var(--blue)"><use href="#droplet"/></svg>Trusted by Local<br>Homeowners &amp;<br>Businesses</li>
  </ul>

  <div class="abs services-pill">OUR SERVICES</div>
  <ul class="abs services-list">
    <li><svg width="9" height="11" color="var(--blue)"><use href="#tickdrop"/></svg>Blocked Drains</li>
    <li><svg width="9" height="11" color="var(--blue)"><use href="#tickdrop"/></svg>Leak Detection &amp;<br>Repairs</li>
    <li><svg width="9" height="11" color="var(--blue)"><use href="#tickdrop"/></svg>Hot Water Systems</li>
    <li><svg width="9" height="11" color="var(--blue)"><use href="#tickdrop"/></svg>Tap &amp; Toilet Repairs</li>
    <li><svg width="9" height="11" color="var(--blue)"><use href="#tickdrop"/></svg>Stormwater Repairs</li>
    <li><svg width="9" height="11" color="var(--blue)"><use href="#tickdrop"/></svg>CCTV Drain<br>Inspections</li>
    <li><svg width="9" height="11" color="var(--blue)"><use href="#tickdrop"/></svg>Gutter &amp; Roof<br>Plumbing</li>
    <li><svg width="9" height="11" color="var(--blue)"><use href="#tickdrop"/></svg>Preventative</li>
    <li><svg width="9" height="11" color="var(--blue)"><use href="#tickdrop"/></svg>Plumbing Maintenance</li>
  </ul>

  <div class="abs reviews-pill">WHAT OUR<br>CUSTOMERS SAY</div>
  <div class="abs review" style="top:511px"><div class="stars">★★★★★</div>“Lachlan from VKD Plumbing cleared our blocked drain quickly and professionally. Highly recommend!”</div>
  <div class="abs review" style="top:571px"><div class="stars">★★★★★</div>"Prompt, reliable and great service. Will definitely use again.”</div>

  <div class="abs contact-box">
    <div class="q">Need a Plumber?</div>
    <div class="n"><b>VKD</b> Plumbing</div>
    <div class="line" style="margin-top:8px"><svg width="10" height="10" fill="#fff"><use href="#phone"/></svg>0491 570 006</div>
    <div class="line"><svg width="10" height="10" color="#fff"><use href="#globe"/></svg>vkdplumbing.com.au</div>
  </div>
  <div class="abs discount">
    <div class="t">NEIGHBOUR DISCOUNT</div>
    <div class="big"><span class="cur">$</span><span class="num">59</span><span class="off">OFF</span></div>
    <div class="r">ANY PLUMBING REPAIR</div>
    <div class="m">(Mention this flyer when booking)</div>
  </div>
</section>

<!-- MAGNET -->
<section class="sheet magnet">
  <div class="brand" style="left:24px;top:48px;font-size:22px">VKD Plumbing</div>
  <div class="abs mag-band"></div>
  <div class="abs mag-foot"></div>
  <svg class="abs mag-art" viewBox="0 0 148 196" role="img" aria-label="Photos of a blocked chrome drain pipe and a coiled jetting hose in droplet frames">
    <svg x="14" y="-8" width="150" height="200" viewBox="0 0 100 140" preserveAspectRatio="none">
      <use href="#teardrop" fill="var(--yellow)"/>
      <g transform="translate(6 8) scale(.88)"><use href="#teardrop" fill="url(#pipeShot)"/></g>
    </svg>
    <svg x="0" y="88" width="80" height="110" viewBox="0 0 100 140" preserveAspectRatio="none">
      <use href="#teardrop" fill="var(--yellow)"/>
      <g transform="translate(8 10) scale(.84)"><use href="#teardrop" fill="#fff"/></g>
      <g transform="translate(14 18) scale(.72)"><use href="#teardrop" fill="url(#hoseShot)"/></g>
    </svg>
  </svg>
  <div class="abs mag-q">Blocked Drains?</div>
  <div class="abs mag-call">Call <b>VKD Plumbing</b></div>
  <div class="abs mag-phone"><svg width="11" height="11" fill="#fff"><use href="#phone"/></svg>0491 570 006</div>
  <div class="abs mag-web"><svg width="10" height="10" color="#fff"><use href="#globe"/></svg>vkdplumbing.com.au</div>
</section>

</body>
</html>
```